Milton Webpage Design

I would like to start an business and management consultancy business. I am thinking to called it "Trovel Consultancy". Besides the consultancy services, I would also like to provide training on finance, forensic accounting, fraud prevention and internal control.
Professional management consultants are contracted by organizations to provide advisory services in an objective and independent manner.

Services include, but are not limited to, strategic planning, facilitation, quality assurance, education and training, investment counsel, identification and analysis of management problems, developing solutions, and the implementation of proposed solutions.

Professional management consultants are hired when an organization lacks sufficient resources, requires external objective advice, or because they have expertise not available within the client organization.

I would like to see the webpage design that use colors apple green with some other contrast color. The design have to be professional look but with a new age touch.

Reason: Unable to find a suitable web pages design

Dear all

Since last week I post a request, but till to date, I has yet to received a new sparkling creative and "wow" web page design. Please help me here!

Regards

Reason: Yet to found a suitable web designer for my web design. Help! I just need a fresh and professional look design. You may ignore the color code I prefer. Send me your sparkling creative work. Thank you so much!

Some examples

```html
<!DOCTYPE html>
<html lang="en">
<head>
<meta charset="utf-8">
<title>Trovel Consultancy</title>
<link href="https://fonts.googleapis.com/css2?family=Questrial&display=swap" rel="stylesheet">
<style>
  :root {
    --apple: #80bd32;
    --apple-deep: #6aa822;
    --ink: #000000;
    --paper: #ffffff;
    --text-dark: #111111;
  }
  html, body { margin: 0; padding: 0; overflow: hidden; background: var(--paper); }
  .page {
    position: relative; width: 814px; height: 1200px; overflow: hidden;
    font-family: "Questrial", "Century Gothic", sans-serif; color: var(--paper);
  }
  .band { position: absolute; left: 0; width: 814px; }
  .band--hero { top: 0; height: 418px; background: var(--apple); }
  .band--welcome { top: 418px; height: 251px; background: var(--ink); }
  .band--field { top: 669px; height: 290px; background: var(--apple); }
  .band--contact { top: 959px; height: 241px; background: var(--ink); }
  .abs { position: absolute; margin: 0; }

  /* brand */
  .brand-disc { position: absolute; left: 84px; top: -59px; width: 152px; height: 152px; border-radius: 50%; background: var(--ink); }
  .brand-name { position: absolute; left: 84px; top: 22px; width: 152px; text-align: center; color: var(--apple); font-size: 17px; line-height: 20px; margin: 0; }

  /* navigation */
  .nav { position: absolute; left: 86px; top: 107px; margin: 0; padding: 0; list-style: none; }
  .nav__rail { position: absolute; left: 97px; top: 120px; height: 164px; border-left: 2px dashed var(--ink); }
  .nav__item { position: relative; height: 41px; display: flex; align-items: center; font-size: 18.5px; color: var(--ink); }
  .nav__dot { width: 16px; height: 16px; border: 2.5px solid var(--ink); border-radius: 50%; background: var(--apple); margin-right: 19px; }
  .nav__item--active .nav__dot { background: var(--ink); box-shadow: inset 0 0 0 3px var(--paper); }
  .tagline { left: 86px; top: 343px; font-size: 22px; line-height: 27px; color: var(--ink); }

  .accent { color: var(--apple); }
  .heading { font-size: 34px; font-weight: 400; line-height: 1; }
  .copy { font-size: 16px; line-height: 22.5px; }

  .read-more {
    position: absolute; width: 78px; height: 78px; border-radius: 50%;
    border: 3px solid; display: flex; align-items: center; justify-content: center;
    text-align: center; font-size: 22px; line-height: 19px;
    box-shadow: 6px 6px 12px rgba(0,0,0,.45);
  }
  .read-more--dark { left: 643px; top: 554px; background: var(--ink); border-color: var(--apple); color: var(--paper); }
  .read-more--light { left: 81px; top: 844px; background: var(--apple); border-color: var(--ink); color: var(--paper); }
  .pin { position: absolute; width: 14px; height: 14px; border-radius: 50%; background: var(--ink); border: 2.5px solid var(--apple); }
  .pin--welcome { left: 679px; top: 409px; }
  .pin--field { left: 117px; top: 658px; border-color: var(--paper); }
  .rail { position: absolute; width: 0; border-left: 2px dashed; }
  .rail--welcome { left: 687px; top: 428px; height: 126px; border-color: var(--apple); }
  .rail--field { left: 125px; top: 677px; height: 167px; border-color: var(--ink); }

  .field-item { position: absolute; font-size: 16px; white-space: nowrap; color: var(--paper); }
  .plus { position: absolute; left: 412px; top: 879px; }
  .plus::before, .plus::after { content: ""; position: absolute; background: var(--apple-deep); box-shadow: 4px 4px 8px rgba(0,0,0,.3); }
  .plus::before { left: -12px; top: -43px; width: 24px; height: 86px; }
  .plus::after { left: -46px; top: -12px; width: 92px; height: 24px; }

  .query { position: absolute; left: 487px; top: 956px; width: 240px; height: 240px; border-radius: 50%; background: var(--apple); }
  .query__title { position: absolute; left: 487px; top: 980px; width: 240px; text-align: center; font-size: 17px; color: var(--text-dark); margin: 0; }
  .query__field { position: absolute; left: 539px; width: 139px; height: 22px; box-sizing: border-box; border: 0; background: var(--paper); color: #8a8a8a; font-family: inherit; font-size: 14.5px; text-align: center; padding: 0; }
  .query__note { position: absolute; left: 563px; top: 1080px; width: 130px; font-size: 6.5px; line-height: 8px; color: var(--ink); margin: 0; }
  .lock { position: absolute; left: 543px; top: 1081px; }
  .submit { position: absolute; left: 565px; top: 1110px; width: 80px; height: 80px; border-radius: 50%; box-sizing: border-box; background: var(--ink); border: 3px solid var(--apple); color: var(--paper); font-family: inherit; font-size: 22px; box-shadow: 0 6px 10px rgba(0,0,0,.4); }
  .copyright { left: 86px; top: 1181px; font-size: 7.5px; color: var(--paper); }
</style>
</head>
<body>
<div class="page">
  <div class="band band--hero"></div>
  <div class="band band--welcome"></div>
  <div class="band band--field"></div>
  <div class="band band--contact"></div>

  <!-- hero lens -->
  <svg class="abs" style="left:0;top:0" width="814" height="430" viewBox="0 0 814 430">
    <polygon points="333,296 353,330 185,426 165,392" fill="var(--apple-deep)"/>
    <circle cx="525" cy="214" r="200" fill="var(--apple)" stroke="var(--apple-deep)" stroke-width="6"/>
    <circle cx="523" cy="216" r="192" fill="none" stroke="var(--ink)" stroke-width="5"/>
    <circle cx="530" cy="210" r="186" fill="var(--paper)"/>
  </svg>
  <div class="abs" role="img" aria-label="Photo of three consultants working at a table with a laptop and papers"
       style="left:344px;top:24px;width:372px;height:372px;border-radius:50%;background:radial-gradient(circle at 55% 40%, #e9e4da 0%, #cfc6b2 45%, #a99e86 75%, #e8e6e2 100%);"></div>

  <div class="brand-disc"></div>
  <p class="brand-name">Trovel Consultancy</p>

  <div class="nav__rail"></div>
  <ul class="nav">
    <li class="nav__item nav__item--active"><span class="nav__dot"></span>HOME</li>
    <li class="nav__item"><span class="nav__dot"></span>ABOUT</li>
    <li class="nav__item"><span class="nav__dot"></span>SERVICES</li>
    <li class="nav__item"><span class="nav__dot"></span>CONTACT</li>
    <li class="nav__item"><span class="nav__dot"></span>ARTICLES &amp; INFORMATION</li>
  </ul>
  <p class="abs tagline">With Trovel,<br>it is more than just a solution</p>

  <!-- welcome -->
  <h1 class="abs heading" style="left:86px;top:460px;">Welcome to <span class="accent">Trovel CONSULTANCY</span></h1>
  <p class="abs copy" style="left:86px;top:528px;width:520px;">Lorem ipsum dolor sit amet, consectetur adipisicing elit, sed do eiusmod tempor incididunt ut labore et dolore magna aliqua. Ut enim ad minim veniam, quis nostrud exercitation ullamco laboris nisi ut aliquip ex ea commodo consequat.</p>
  <div class="rail rail--welcome"></div>
  <div class="pin pin--welcome"></div>
  <div class="read-more read-more--dark">read<br>more</div>

  <!-- field -->
  <h2 class="abs heading" style="right:84px;top:700px;color:var(--text-dark);">Our field</h2>
  <span class="field-item" style="left:213px;top:751px;">strategic planning</span>
  <span class="field-item" style="left:416px;top:751px;">investment counsel</span>
  <span class="field-item" style="left:634px;top:751px;">facilitation</span>
  <span class="field-item" style="left:286px;top:787px;">education and training</span>
  <span class="field-item" style="left:531px;top:787px;">quality assurance</span>
  <div class="plus"></div>
  <span class="field-item" style="left:251px;top:869px;">identification</span>
  <span class="field-item" style="left:469px;top:867px;">analysis of management problems</span>
  <span class="field-item" style="left:224px;top:899px;">developing solutions</span>
  <span class="field-item" style="left:436px;top:899px;">implementation of proposed solutions</span>
  <div class="rail rail--field"></div>
  <div class="pin pin--field"></div>
  <div class="read-more read-more--light">read<br>more</div>

  <!-- contact -->
  <h2 class="abs heading" style="left:86px;top:990px;">Get in <span class="accent">Touch</span></h2>
  <p class="abs copy" style="left:86px;top:1059px;">trovel is always at your service.<br>Request a consultancy session<br>by either calling us or<br>filling out our query form.</p>

  <form class="query-form">
    <div class="query"></div>
    <p class="query__title">QUERY FORM</p>
    <input class="query__field" style="top:1011px;" type="email" placeholder="enter your email" aria-label="Email">
    <input class="query__field" style="top:1044px;" type="tel" placeholder="enter your phone" aria-label="Phone">
    <svg class="lock" width="12" height="16" viewBox="0 0 12 16" aria-hidden="true">
      <path d="M3 7V4.5a3 3 0 0 1 6 0V7" fill="none" stroke="var(--ink)" stroke-width="2"/>
      <rect x="0" y="7" width="12" height="9" rx="1" fill="var(--ink)"/>
    </svg>
    <p class="query__note">your data is strictly private and will be used only for the above purpose.</p>
    <button class="submit" type="button">submit</button>
  </form>

  <p class="abs copyright">Copyright © 2013 trovel CONSULTANCY - All Rights Reserved</p>
</div>
</body>
</html>
```